Norlo Tiered Food/Dessert Trays Spec Sheet

We need an elegant spec sheet template to use with our food/dessert trays. This will accompany the item when it ships out and on the web. It is something we would like to email our customers when they are considering our different banquet trays. It is important that it does not look too retail. We are the manufacturer and do not sell retail. We are business to business. It needs to help a salesman make a sale and look elegant enough while conveying the info to them.
Updates

Target Market(s)

Banquet Halls, Caterers, Country Clubs, Wedding and event centers.

Industry/Entity Type

Event

Font styles to use
Serif
Decorative
Script

Requirements
Must have
• All the copy in the word doc. Also use the model name as the heading at the top of the sheet
Nice to have
• An elegant but professional look
Should not have
• Not too busy

```html
<!DOCTYPE html>
<html lang="en">
<head>
<meta charset="utf-8">
<title>Norlo Fountains – Regal Deluxe Spec Sheet</title>
<link rel="stylesheet" href="https://fonts.googleapis.com/css2?family=Arimo:wght@400;700&display=swap">
<style>
  :root {
    --brand-purple: #3b2a6d;
    --ink: #1f1f1f;
    --rule: #8c8c8c;
    --paper: #ffffff;
    --photo-warm-dark: #3a2412;
    --photo-warm-mid: #9a6a35;
    --photo-warm-light: #e6c49a;
    --steel-light: #eeeeee;
    --steel-dark: #8d8d8d;
  }
  * { margin: 0; padding: 0; box-sizing: border-box; }
  html, body { width: 859px; height: 1200px; overflow: hidden; background: var(--paper); }
  body { font-family: "Arimo", Arial, sans-serif; color: var(--ink); position: relative; }

  .sheet { position: relative; width: 859px; height: 1200px; overflow: hidden; }

  .banquet-photo {
    position: absolute; left: 0; top: 136px; width: 859px; height: 415px;
    background: linear-gradient(135deg, var(--photo-warm-dark) 0%, var(--photo-warm-mid) 45%, var(--photo-warm-light) 75%, var(--photo-warm-mid) 100%);
  }

  .title-ribbon { position: absolute; left: 62px; top: 0; width: 306px; height: 628px; }
  .title-ribbon svg { position: absolute; inset: 0; }

  .brand-mark {
    position: absolute; left: 0; top: 64px; width: 306px;
    display: flex; align-items: center; justify-content: center; gap: 12px;
    color: var(--paper);
  }
  .brand-mark .dot { width: 38px; height: 38px; border-radius: 50%; background: var(--paper); }
  .brand-mark .name { font-size: 30px; font-weight: 400; line-height: 1.05; letter-spacing: 1px; }
  .brand-mark .name span { display: block; font-size: 19px; letter-spacing: 1.5px; }

  .ribbon-copy {
    position: absolute; left: 8px; top: 189px; width: 290px;
    color: var(--paper); font-weight: 700; font-size: 15px; line-height: 23.6px;
    text-align: center; white-space: nowrap;
  }

  .product-photo {
    position: absolute; left: 54px; top: 612px; width: 327px; height: 376px;
    background: radial-gradient(ellipse at 50% 55%, var(--steel-light) 0%, #c9c9c9 45%, var(--steel-dark) 100%);
    border-radius: 50% 50% 12px 12px / 40% 40% 12px 12px;
    opacity: .85;
  }

  .specs { position: absolute; left: 464px; top: 579px; width: 309px; }
  .section-title { color: var(--brand-purple); font-size: 17px; font-weight: 700; letter-spacing: .3px; margin-bottom: 8px; }
  .spec-table { width: 100%; border-collapse: collapse; font-size: 13.5px; }
  .spec-table tr + tr td { border-top: 1px solid var(--rule); }
  .spec-table td { height: 31px; vertical-align: middle; white-space: nowrap; }
  .spec-table td.label { font-weight: 700; width: 194px; }

  .features { position: absolute; left: 464px; top: 847px; width: 360px; }
  .feature-list { list-style: none; font-size: 13.5px; margin-top: 4px; }
  .feature-list li { height: 28px; line-height: 28px; }
  .feature-list li::before { content: "•"; color: var(--brand-purple); margin-right: 6px; }

  .contact-bar {
    position: absolute; left: 0; top: 1117px; width: 859px; height: 83px;
    background: var(--brand-purple); color: var(--paper); padding: 21px 0 0 75px;
  }
  .contact-bar .company { font-size: 13.5px; font-weight: 700; margin-bottom: 7px; }
  .contact-bar .lines { font-size: 13.5px; white-space: nowrap; }
  .contact-bar .lines b { font-weight: 700; }
  .contact-bar .sep { margin: 0 11px; }
</style>
</head>
<body>
<main class="sheet">
  <div class="banquet-photo" role="img" aria-label="Candlelit banquet hall with a long dressed table, gold chairs and floral centrepieces"></div>

  <header class="title-ribbon">
    <svg width="306" height="628" viewBox="0 0 306 628" aria-hidden="true">
      <polygon points="0,0 306,0 306,628 153,567 0,628" fill="var(--brand-purple)"/>
    </svg>
    <div class="brand-mark">
      <div class="dot"></div>
      <div class="name">NORLO<span>FOUNTAINS</span></div>
    </div>
    <p class="ribbon-copy">The Regal Deluxe Three-Tier Buffet<br>Stand Features Polished, Stain-<br>less Steel, Trays and Base. It<br>Also Features Bright Nickel<br>Plated Silver Columns. This Eye<br>Catching Stand with its Large<br>Tray Sizes Make it an Excellent<br>Choice for Serving Large Groups<br>at Banquets, Buffets or any<br>Catering Operation. Create<br>Stunning Appetizers, Finger<br>Foods, Main Courses and More.<br>This Stand is a True Caterers<br>Dream...</p>
  </header>

  <div class="product-photo" role="img" aria-label="Three-tier polished stainless steel buffet stand with nickel columns and a finial on top"></div>

  <section class="specs">
    <h2 class="section-title">PRODUCT SPECS</h2>
    <table class="spec-table">
      <tr><td class="label">Model #</td><td>NRL-T3-0907-K</td></tr>
      <tr><td class="label">Model Name</td><td>Regal Deluxe</td></tr>
      <tr><td class="label">Height</td><td>33”</td></tr>
      <tr><td class="label">Tray Sizes</td><td>24”, 18”, 14”</td></tr>
      <tr><td class="label">Product Weight</td><td>20lbs</td></tr>
      <tr><td class="label">Shipping Weight</td><td>28lbs</td></tr>
      <tr><td class="label">Shipping Dimensions</td><td>27 x 27 x 10 Inches</td></tr>
    </table>
  </section>

  <section class="features">
    <h2 class="section-title">FEATURES</h2>
    <ul class="feature-list">
      <li>Designed for Repeated Commercial Use</li>
      <li>High Polished Stainless Steel Trays &amp; Base</li>
      <li>Decorative Silver Bow Tie Trim on the Base</li>
      <li>Nickel Plated Silver Columns ( No Tarnish, No Polish )</li>
      <li>Self-Serving Buffet Station</li>
      <li>No Tools Needed for Assembly or Disassembly</li>
      <li>Breaks Down for Easy Clean Up and Storage</li>
      <li>1 Year Limited Warranty</li>
    </ul>
  </section>

  <footer class="contact-bar">
    <p class="company">NORLO FOUNTAIN SALES, INC.</p>
    <p class="lines"><b>Web:</b> www.norlofountains.com<span class="sep">|</span><b>Phone:</b> 800-555-0142<span class="sep">|</span><b>Fax:</b> 215-555-0187<span class="sep">|</span><b>Email:</b> Info@norlofountains.com</p>
  </footer>
</main>
</body>
</html>
```